Consulting Company Business Card

I am looking for a minimalist, classy, professional design on my business card. I would like it to be double-sided. I want to use the font and color scheme of my logo which are attached. Please be creative in the designs that you send me. I want to play off the design of my logo with the inner C that is Green and Blue broken up with the white.
Target Market(s)
Small Businesses
Industry/Entity Type
Consulting
Contact Information for Business Card
Dale M. Whitcombe, CPA CGMA, 555-014-2873, dwhitcombe@vorantaadvisory.example, www.vorantaadvisory.example

```html
<!DOCTYPE html>
<html lang="en">
<head>
<meta charset="utf-8">
<title>Voranta Advisory – Business Card</title>
<link rel="stylesheet" href="https://fonts.googleapis.com/css2?family=Montserrat:wght@400;500;700;800&display=swap">
<style>
  :root {
    --stage: #e9ebec;
    --teal: #2a8a88;
    --teal-light: #5aaaa8;
    --teal-deep: #1f7674;
    --navy: #2a2f58;
    --ink: #2b2b2b;
    --paper: #ffffff;
  }
  * { box-sizing: border-box; margin: 0; padding: 0; }
  html, body { width: 1200px; height: 1012px; overflow: hidden; }
  body {
    background: var(--stage);
    font-family: "Montserrat", Arial, sans-serif;
    display: flex;
    flex-direction: column;
    align-items: center;
    justify-content: center;
    gap: 40px;
  }
  .card {
    position: relative;
    width: 780px;
    height: 446px;
    overflow: hidden;
    box-shadow: 0 6px 18px rgba(0,0,0,0.18);
  }
  .card-front {
    background: linear-gradient(135deg, var(--teal-deep), var(--teal) 55%, var(--teal-light));
    display: flex;
    align-items: center;
    justify-content: center;
  }
  .wordmark {
    font-weight: 800;
    text-align: center;
    text-transform: uppercase;
    line-height: 1;
  }
  .card-front .wordmark { color: var(--paper); }
  .wordmark .primary { display: block; font-size: 92px; letter-spacing: 2px; }
  .wordmark .secondary { display: block; font-size: 30px; letter-spacing: 12px; margin-top: 10px; }

  .card-back { background: var(--paper); }
  .card-back .wave { position: absolute; inset: 0; width: 100%; height: 100%; }
  .card-back .wordmark {
    position: absolute;
    right: 56px;
    top: 190px;
    color: var(--navy);
  }
  .card-back .wordmark .primary { font-size: 52px; }
  .card-back .wordmark .secondary { font-size: 17px; letter-spacing: 8px; margin-top: 6px; }

  .contact {
    position: absolute;
    left: 40px;
    bottom: 34px;
    color: var(--ink);
  }
  .contact .name {
    color: var(--teal);
    font-weight: 700;
    font-size: 21px;
    line-height: 1.2;
    text-transform: uppercase;
    letter-spacing: 0.5px;
  }
  .contact .title { font-size: 16px; font-weight: 500; line-height: 1.2; margin: 2px 0 16px 18px; }
  .contact ul { list-style: none; margin-left: 18px; }
  .contact li {
    display: flex;
    align-items: center;
    gap: 12px;
    font-size: 15px;
    line-height: 1.2;
    margin-bottom: 8px;
  }
  .contact li:last-child { margin-bottom: 0; }
  .contact li svg { width: 16px; height: 16px; flex: none; }
</style>
</head>
<body>
  <section class="card card-front" aria-label="Card front">
    <div class="wordmark">
      <span class="primary">Voranta</span>
      <span class="secondary">Advisory</span>
    </div>
  </section>

  <section class="card card-back" aria-label="Card back">
    <svg class="wave" viewBox="0 0 780 446" preserveAspectRatio="none" aria-hidden="true">
      <defs>
        <linearGradient id="tealFill" x1="0" y1="0" x2="1" y2="1">
          <stop offset="0" stop-color="var(--teal-light)"/>
          <stop offset="1" stop-color="var(--teal)"/>
        </linearGradient>
      </defs>
      <path class="wave-teal" d="M0 0 H530 C450 25 410 100 340 145 C260 195 130 200 0 180 Z" fill="url(#tealFill)"/>
      <path class="wave-navy" d="M0 190 C130 210 270 200 350 155 C420 115 460 30 545 0 H566 C480 30 440 120 360 175 C280 225 140 232 0 225 Z" fill="var(--navy)"/>
    </svg>

    <div class="wordmark">
      <span class="primary">Voranta</span>
      <span class="secondary">Advisory</span>
    </div>

    <div class="contact">
      <p class="name">Dale M. Whitcombe</p>
      <p class="title">CPA CGMA</p>
      <ul>
        <li>
          <svg viewBox="0 0 16 16" aria-hidden="true"><circle cx="8" cy="8" r="8" fill="var(--teal)"/><path d="M5 4.5 L6.5 4.2 L7.3 6.2 L6.4 7 C6.9 8 7.8 8.9 8.9 9.5 L9.7 8.6 L11.7 9.4 L11.4 11 C8 11.4 4.6 8 5 4.5 Z" fill="#fff"/></svg>
          555-014-2873
        </li>
        <li>
          <svg viewBox="0 0 16 16" aria-hidden="true"><rect x="1" y="3" width="14" height="10" rx="1" fill="var(--teal)"/><path d="M1.5 3.5 L8 9 L14.5 3.5" stroke="#fff" stroke-width="1.3" fill="none"/></svg>
          dwhitcombe@vorantaadvisory.example
        </li>
        <li>
          <svg viewBox="0 0 16 16" aria-hidden="true"><circle cx="8" cy="8" r="7.5" fill="var(--teal)"/><ellipse cx="8" cy="8" rx="3" ry="7" stroke="#fff" stroke-width="1" fill="none"/><path d="M1 8 H15" stroke="#fff" stroke-width="1"/></svg>
          www.vorantaadvisory.example
        </li>
      </ul>
    </div>
  </section>
</body>
</html>
```